Marla Quint Memoir

Book Cover Design
Title: Cedars and Salt
Subtitle: One Girl's Climb Through Kinship and Mercy
Author: Marla Quint
Book Description: Marla Quint’s memoir Cedars and Salt, follows five generations of one Alaskan family evolving with the rapidly changing landscape of the North. Few memoirs combine love of nature with love of family so eloquently, while at the same time acknowledging that each carries the potential for so much loss and pain. Through it all, this is the story of one woman’s quest to carve a place for herself in a rapidly changing land and claim her own unique power.
INSTRUCTIONS: Open to any interesting creative designs reflecting the above description. However, MUST include the attached photo on the cover in some way. Have also attached the .indd template for reference. Please leave bleed area plus 1/2 inch all around. On spine, leave two inches at bottom to allow for publisher's logo.

```html
<!DOCTYPE html>
<html lang="en">
<head>
<meta charset="utf-8">
<title>Cedars and Salt — Marla Quint</title>
<link rel="stylesheet" href="https://fonts.googleapis.com/css2?family=Bebas+Neue&family=Oswald:wght@400;600&display=swap">
<style>
  :root {
    --page: #ffffff;
    --sky-high: #a9b8c3;
    --sky-mist: #c9d3d8;
    --mountain: #1c3144;
    --ice: #e4eaee;
    --ice-shadow: #b9c6ce;
    --water-deep: #34414c;
    --hair: #6b5240;
    --blouse: #d9c3ad;
    --blouse-shade: #b89a80;
    --title-fill: #7b3c41;
    --title-edge: #dca45c;
    --subtitle-ink: #141414;
    --author-ink: #bcd2e2;
  }
  * { margin: 0; padding: 0; box-sizing: border-box; }
  html, body {
    width: 1200px;
    height: 1200px;
    overflow: hidden;
    background: var(--page);
  }
  .book-cover {
    position: absolute;
    left: 247px;
    top: 60px;
    width: 707px;
    height: 1079px;
    overflow: hidden;
  }
  .landscape-photo {
    position: absolute;
    inset: 0;
    background:
      radial-gradient(ellipse 60% 24% at 92% 44%, var(--mountain) 0%, rgba(28,49,68,0.85) 50%, rgba(28,49,68,0) 100%),
      radial-gradient(ellipse 40% 10% at 30% 54%, rgba(40,62,84,0.9) 0%, rgba(40,62,84,0) 100%),
      linear-gradient(180deg,
        var(--sky-high) 0%,
        var(--sky-mist) 36%,
        #8c9eac 46%,
        #3a5064 53%,
        var(--ice) 57%,
        var(--ice-shadow) 70%,
        #7d8a94 82%,
        var(--water-deep) 100%);
  }
  .portrait-photo {
    position: absolute;
    left: 185px;
    top: 477px;
    width: 381px;
    height: 602px;
    border-radius: 40% 40% 8% 8% / 22% 22% 0 0;
    background:
      linear-gradient(180deg,
        var(--hair) 0%,
        #8a6d58 28%,
        var(--blouse) 48%,
        var(--blouse-shade) 100%);
  }
  .subtitle {
    position: absolute;
    top: 44px;
    left: 0;
    width: 100%;
    text-align: center;
    font-family: "Oswald", sans-serif;
    font-weight: 400;
    font-size: 24px;
    letter-spacing: 2.2px;
    color: var(--subtitle-ink);
    text-transform: uppercase;
  }
  .title {
    position: absolute;
    top: 121px;
    left: 0;
    width: 100%;
    text-align: center;
    font-family: "Bebas Neue", sans-serif;
    font-weight: 400;
    font-size: 224px;
    line-height: 176px;
    color: var(--title-fill);
    -webkit-text-stroke: 2px var(--title-edge);
    text-shadow: 0 4px 8px rgba(0,0,0,0.35);
    text-transform: uppercase;
  }
  .title-line { display: block; }
  .title-line--first { letter-spacing: 8px; }
  .title-line--second { letter-spacing: 2px; transform: scaleX(0.88); }
  .author {
    position: absolute;
    top: 486px;
    right: 62px;
    font-family: "Oswald", sans-serif;
    font-weight: 600;
    font-size: 36px;
    letter-spacing: 1px;
    color: var(--author-ink);
    font-variant: small-caps;
  }
</style>
</head>
<body>
  <div class="book-cover">
    <div class="landscape-photo" role="img" aria-label="Icy glacial bay with floating ice and misty dark mountains under a grey sky"></div>
    <div class="portrait-photo" role="img" aria-label="Photograph of a woman with long brown hair in a floral blouse standing at the water's edge"></div>
    <p class="subtitle">One Girl's Climb Through Kinship and Mercy</p>
    <h1 class="title">
      <span class="title-line title-line--first">Cedars</span>
      <span class="title-line title-line--second">and Salt</span>
    </h1>
    <p class="author">Marla Quint</p>
  </div>
</body>
</html>
```